UI Redesign For Mobile Events iPhone App

We need a new UI design for our Social Events mobile app. Our app called Vrenn is geared to help users find trending events in their local area. We show visual metrics on percent full and male female ratio and age group ratings. We want people to see whats going on at event before they get there through our app. Also we have a group chat portion to our app that we need included in the design. We would like to see a fresh, clean, and easy to use user interface that uses colors like, purple, blue and or hot pink.You may visit our website myvrenn.example for more information about what our app is geared to do.
Updates

Target Market(s)

Our target market people that use social networks and attend social events ranging from ages 16-44.

Industry/Entity Type

Events

Requirements
Must have
• We would like to see an Example layout of all screens. (UPDATE: Please use our current background in your design, A PSD has been uploaded for you to grab the background. The Vrenn Logo is NOT required to be included at the top of every screen)

-Profile Screen: Shows points earned, events attending, events created
-Event Listings Screen: Must have large image for event, visual metrics, date& time, location, attend button, invite friends button, Label for user who created the event
-Event Description Page: Shows everything as the event listing, has a description of the event, shows friends that are attending, points available
-Group Messaging Screen
-Slide Out Navigation Screen
-Notification Screen
-Ticket Screen
-Friends Activity Screen
-Friends Profile View: Shows events they've attended and points they've earned under their contact picture; invite button
-Sign-In Screen
-Register Screen

A way to label/categorize our different types of events:
-Nightlife
-Family
-Live Music & Concerts
-Restaurants
Group Chat Layout
Visual Meters for Percent Full, Male Female Ratio, Age Rating

```html
<!DOCTYPE html>
<html lang="en">
<head>
<meta charset="utf-8">
<title>Vrenn – App screen UI</title>
<link rel="stylesheet" href="https://fonts.googleapis.com/css2?family=Source+Sans+3:wght@300;400;600&family=Yanone+Kaffeesatz:wght@300;400&display=swap">
<style>
  :root{
    --stage:#262b3f;
    --purple:#9554b5;
    --purple-deep:#7a2d95;
    --purple-bright:#b21ee0;
    --blue:#00a9e8;
    --pink:#ff93ee;
    --lilac:#d9b8ee;
    --white:#ffffff;
    --ink:#222222;
    --grey:#9a9a9a;
    --track:#ece0f3;
  }
  *{box-sizing:border-box;margin:0;padding:0}
  html,body{width:1200px;height:900px;overflow:hidden;background:var(--stage)}
  body{font-family:"Source Sans 3",sans-serif;color:var(--white);position:relative}

  .board-title{position:absolute;top:40px;left:0;width:1200px;text-align:center;font-weight:400;font-size:30px;letter-spacing:.5px}

  .screen-grid{position:absolute;top:110px;left:225px;display:grid;grid-template-columns:repeat(3,210px);grid-template-rows:repeat(2,370px);column-gap:60px;row-gap:30px}
  .screen{position:relative;width:210px;height:370px;background:var(--purple);overflow:hidden;box-shadow:0 10px 24px rgba(0,0,0,.45)}

  /* sign-in */
  .field{position:absolute;left:18px;width:174px;height:62px;background:var(--white);border-radius:12px;display:flex;align-items:center;gap:12px;padding-left:14px;color:var(--grey);font-weight:300;font-size:19px}
  .field--user{top:22px}
  .field--pass{top:100px}
  .field__icon{width:22px;height:24px;flex:none}
  .field__spacer{width:22px;flex:none}
  .auth-band{position:absolute;left:0;bottom:0;width:100%;height:140px;background:var(--blue);display:flex;align-items:center;justify-content:center;gap:26px;font-weight:300;font-size:22px}

  /* categories */
  .category{display:flex;align-items:center;gap:14px;padding-left:16px;height:92.5px;font-size:17px;font-weight:400}
  .category--active{background:var(--blue)}
  .category__icon{width:36px;height:36px;flex:none}
  .screen--tabbed .category{height:80px}

  .tabbar{position:absolute;left:0;bottom:0;width:100%;height:50px;background:var(--purple-deep);display:grid;grid-template-columns:repeat(4,1fr) 42px}
  .tab{display:flex;flex-direction:column;align-items:center;justify-content:center;gap:3px;font-size:7px;font-weight:400;white-space:nowrap}
  .tab svg{width:18px;height:16px}
  .tab--settings{background:var(--purple)}
  .tab--settings svg{width:20px;height:20px}

  /* chat */
  .chat-title{position:absolute;top:10px;right:18px;font-family:"Yanone Kaffeesatz",sans-serif;font-weight:300;font-size:42px}
  .chat-subtitle{position:absolute;top:70px;left:16px;font-size:10px;font-weight:300}
  .msg{position:absolute;display:flex;align-items:center;gap:8px}
  .avatar{width:30px;height:30px;border-radius:4px;flex:none}
  .avatar--grey{background:linear-gradient(135deg,#5d5d5d,#a7a7a7)}
  .avatar--warm{background:linear-gradient(135deg,#b88a72,#e6cbb6)}
  .bubble{border-radius:8px;padding:5px 10px;font-size:10px;white-space:nowrap}
  .bubble--in{background:var(--white);color:var(--ink)}
  .bubble--out{background:var(--purple-bright);color:var(--white)}
  .bubble--typing{letter-spacing:1px;font-weight:600}
  .msg--one{top:110px;left:14px}
  .msg--reply{top:150px;right:14px}
  .msg--two{top:200px;left:50px}
  .friends-band{position:absolute;left:0;bottom:0;width:100%;height:90px;background:var(--purple-deep);display:flex;align-items:flex-end;gap:8px;padding:0 0 12px 14px}
  .friends-band .avatar{width:40px;height:40px}
  .friends-band__note{margin-left:auto;align-self:flex-start;padding:14px 14px 0 0;font-size:9px;font-weight:300}

  /* splash */
  .brand{position:absolute;top:96px;left:24px;display:flex;align-items:center;gap:10px;font-weight:300;font-size:26px;letter-spacing:2px}
  .brand__dot{width:34px;height:34px;border-radius:50%;background:var(--lilac)}
  .tagline{position:absolute;top:170px;left:24px;font-weight:300;font-size:30px;line-height:1.15}

  /* stats */
  .stats-top{position:absolute;top:0;left:0;width:100%;height:250px}
  .meters{position:absolute;left:0;bottom:0;width:100%;height:120px;background:var(--white);color:var(--ink);font-size:10px;padding:10px 14px;display:grid;grid-template-columns:1fr 1fr;column-gap:12px}
  .meter{display:flex;flex-direction:column;gap:4px}
  .meter__label{font-weight:600;letter-spacing:.5px}
  .bar{height:9px;background:var(--track);position:relative}
  .bar__fill{position:absolute;inset:0 auto 0 0;background:var(--purple)}
  .age-row{display:flex;align-items:center;gap:6px}
  .age-row .bar{flex:1}
  .age-row span{width:20px;text-align:right}
</style>
</head>
<body>
  <h1 class="board-title">App screen UI</h1>

  <main class="screen-grid">
    <section class="screen screen--signin" aria-label="Sign-in screen">
      <div class="field field--user">
        <svg class="field__icon" viewBox="0 0 22 24" aria-hidden="true"><path d="M6 10V7a5 5 0 0 1 10 0v3" fill="none" stroke="var(--lilac)" stroke-width="2"/><rect x="2" y="10" width="18" height="13" rx="2" fill="none" stroke="var(--lilac)" stroke-width="2"/></svg>
        Username
      </div>
      <div class="field field--pass"><span class="field__spacer"></span>Password</div>
      <div class="auth-band"><span>sign in</span><span>register</span></div>
    </section>

    <section class="screen screen--categories" aria-label="Event categories">
      <div class="category">
        <svg class="category__icon" viewBox="0 0 36 36" aria-hidden="true"><path d="M8 4v10M12 4v10M16 4v10M8 14h8M12 14v18" stroke="#fff" stroke-width="2.4" fill="none"/><path d="M24 4c5 2 5 12 0 14v14" stroke="#fff" stroke-width="3" fill="none"/></svg>
        Restaurants
      </div>
      <div class="category">
        <svg class="category__icon" viewBox="0 0 36 36" aria-hidden="true"><path d="M4 6h24L16 20zM16 20v10M10 31h12" stroke="#fff" stroke-width="2.4" fill="none"/><circle cx="28" cy="30" r="3" fill="#fff"/></svg>
        Nightlife
      </div>
      <div class="category category--active">
        <svg class="category__icon" viewBox="0 0 36 36" aria-hidden="true"><path d="M6 8l10 16 10-16z" stroke="#fff" stroke-width="2.4" fill="none"/><path d="M16 24c0 6-8 4-8 9M20 26c4 2 6 5 4 8" stroke="#fff" stroke-width="2" fill="none"/></svg>
        Live concerts
      </div>
      <div class="category">
        <svg class="category__icon" viewBox="0 0 36 36" aria-hidden="true"><g fill="#fff"><circle cx="8" cy="7" r="3"/><rect x="5" y="11" width="6" height="20" rx="2"/><circle cx="18" cy="7" r="3"/><rect x="15" y="11" width="6" height="20" rx="2"/><circle cx="28" cy="15" r="2.5"/><rect x="25.5" y="18.5" width="5" height="12" rx="2"/></g></svg>
        Family
      </div>
    </section>

    <section class="screen screen--chat" aria-label="Group chat">
      <h2 class="chat-title">Chats</h2>
      <p class="chat-subtitle">Group chat with Theo and Marc.</p>
      <div class="msg msg--one">
        <div class="avatar avatar--grey" role="img" aria-label="Friend profile photo"></div>
        <div class="bubble bubble--in">Do you know about Vrenn?</div>
      </div>
      <div class="msg msg--reply">
        <div class="bubble bubble--out">Yeah, its a cool app !</div>
        <div class="avatar avatar--warm" role="img" aria-label="Friend profile photo"></div>
      </div>
      <div class="msg msg--two">
        <div class="avatar avatar--grey" role="img" aria-label="Friend profile photo"></div>
        <div class="bubble bubble--out bubble--typing">•••</div>
      </div>
      <div class="friends-band">
        <div class="avatar avatar--grey" role="img" aria-label="Friend profile photo"></div>
        <div class="avatar avatar--warm" role="img" aria-label="Friend profile photo"></div>
        <span class="friends-band__note">add more friends</span>
      </div>
    </section>

    <section class="screen screen--splash" aria-label="Welcome screen">
      <div class="brand"><span class="brand__dot"></span>VRENN</div>
      <p class="tagline">events at your fingertips !</p>
    </section>

    <section class="screen screen--stats" aria-label="Event metrics">
      <svg class="stats-top" viewBox="0 0 210 250" aria-hidden="true">
        <g transform="translate(70 72)">
          <circle r="52" fill="none" stroke="rgba(255,255,255,.25)" stroke-width="1"/>
          <circle r="52" fill="none" stroke="var(--blue)" stroke-width="10" stroke-dasharray="209 327" transform="rotate(-90)"/>
          <text y="-4" font-size="15" font-family="Source Sans 3, sans-serif" font-weight="300" fill="#fff" text-anchor="middle">64%</text>
          <text y="16" font-size="15" font-family="Source Sans 3, sans-serif" font-weight="300" fill="#fff" text-anchor="middle">MALES</text>
        </g>
        <g transform="translate(140 185)">
          <circle r="42" fill="none" stroke="rgba(255,255,255,.25)" stroke-width="1"/>
          <circle r="42" fill="none" stroke="var(--pink)" stroke-width="8" stroke-dasharray="132 264" transform="rotate(-90)"/>
          <text y="-4" font-size="13" font-family="Source Sans 3, sans-serif" font-weight="300" fill="#fff" text-anchor="middle">50%</text>
          <text y="13" font-size="13" font-family="Source Sans 3, sans-serif" font-weight="300" fill="#fff" text-anchor="middle">FEMALES</text>
        </g>
      </svg>
      <div class="meters">
        <div class="meter">
          <span class="meter__label">FULL</span>
          <div class="bar"><div class="bar__fill" style="width:30%"></div></div>
          <div class="bar"><div class="bar__fill" style="width:65%"></div></div>
          <span class="meter__label">EMPTY</span>
        </div>
        <div class="meter">
          <span class="meter__label">AGE ALLOWED</span>
          <div class="age-row"><div class="bar"></div><span>21+</span></div>
          <div class="age-row"><div class="bar"><div class="bar__fill" style="width:40%"></div></div><span>18+</span></div>
          <div class="age-row"><div class="bar"><div class="bar__fill" style="width:100%"></div></div><span>5+</span></div>
        </div>
      </div>
    </section>

    <section class="screen screen--categories screen--tabbed" aria-label="Event categories with navigation">
      <div class="category">
        <svg class="category__icon" viewBox="0 0 36 36" aria-hidden="true"><path d="M8 4v10M12 4v10M16 4v10M8 14h8M12 14v18" stroke="#fff" stroke-width="2.4" fill="none"/><path d="M24 4c5 2 5 12 0 14v14" stroke="#fff" stroke-width="3" fill="none"/></svg>
        Restaurants
      </div>
      <div class="category">
        <svg class="category__icon" viewBox="0 0 36 36" aria-hidden="true"><path d="M4 6h24L16 20zM16 20v10M10 31h12" stroke="#fff" stroke-width="2.4" fill="none"/><circle cx="28" cy="30" r="3" fill="#fff"/></svg>
        Nightlife
      </div>
      <div class="category category--active">
        <svg class="category__icon" viewBox="0 0 36 36" aria-hidden="true"><path d="M6 8l10 16 10-16z" stroke="#fff" stroke-width="2.4" fill="none"/><path d="M16 24c0 6-8 4-8 9M20 26c4 2 6 5 4 8" stroke="#fff" stroke-width="2" fill="none"/></svg>
        Live concerts
      </div>
      <div class="category">
        <svg class="category__icon" viewBox="0 0 36 36" aria-hidden="true"><g fill="#fff"><circle cx="8" cy="7" r="3"/><rect x="5" y="11" width="6" height="20" rx="2"/><circle cx="18" cy="7" r="3"/><rect x="15" y="11" width="6" height="20" rx="2"/><circle cx="28" cy="15" r="2.5"/><rect x="25.5" y="18.5" width="5" height="12" rx="2"/></g></svg>
        Family
      </div>
      <nav class="tabbar">
        <div class="tab"><svg viewBox="0 0 18 16" aria-hidden="true"><circle cx="9" cy="5" r="4" fill="#fff"/><path d="M1 16c0-5 16-5 16 0z" fill="#fff"/></svg>profile</div>
        <div class="tab"><svg viewBox="0 0 18 16" aria-hidden="true"><path d="M6 2v12M12 2v12M6 8h6" stroke="#fff" stroke-width="1.6" fill="none"/></svg>my vrenns</div>
        <div class="tab"><svg viewBox="0 0 18 16" aria-hidden="true"><rect x="1" y="2" width="16" height="13" fill="none" stroke="#fff" stroke-width="1.4"/><path d="M1 6h16M5 9h2M9 9h2M13 9h2M5 12h2M9 12h2" stroke="#fff" stroke-width="1.4"/></svg>events</div>
        <div class="tab"><svg viewBox="0 0 18 16" aria-hidden="true"><path d="M3 10l8-9 5 5-9 8z" fill="#fff"/></svg>tickets</div>
        <div class="tab tab--settings"><svg viewBox="0 0 20 20" aria-hidden="true"><circle cx="10" cy="10" r="6" fill="none" stroke="#fff" stroke-width="3" stroke-dasharray="3 1.7"/><circle cx="10" cy="10" r="3.2" fill="none" stroke="#fff" stroke-width="2"/></svg></div>
      </nav>
    </section>
  </main>
</body>
</html>
```